Upscale dog care facility need some marketing material

We offer a lot of services for dogs and their humans. We have a large indoor dog park, swimming pools, dog daycare and boarding, Pet CPR/First Aid classes and training. We love the trifold brochures where we can highlight all of our services (even a few pics of the facility) as well as give everyone information on our pricing and membership concepts. Will primarily be used for marketing to vets and local pet stores to help get the word out about our business.

```html
<!DOCTYPE html>
<html lang="en">
<head>
<meta charset="utf-8">
<title>Splash &amp; Stroll – Trifold Brochure</title>
<link href="https://fonts.googleapis.com/css2?family=Open+Sans:ital,wght@0,300;0,400;0,600;1,400&display=swap" rel="stylesheet">
<style>
  :root{
    --backdrop:#e4e5e7;
    --paper:#ffffff;
    --ocean:#2aa1d3;
    --ocean-light:#63c6ec;
    --deep:#1479a8;
    --teal:#1b8cb4;
    --ink:#1f2a33;
    --muted:#4b5a66;
    --grass:#8cc63f;
  }
  *{box-sizing:border-box;margin:0;padding:0}
  html,body{width:1200px;height:2400px;overflow:hidden}
  body{background:var(--backdrop);font-family:"Open Sans",Arial,sans-serif;color:var(--ink);position:relative}
  .spread{position:absolute;left:50px;width:1100px;height:850px;background:var(--paper);box-shadow:0 6px 24px rgba(0,0,0,.12);overflow:hidden}
  .spread--outside{top:250px}
  .spread--inside{top:1300px}
  .spread svg.artwork{position:absolute;inset:0;width:1100px;height:850px}
  .block{position:absolute}
  .heading-light{font-weight:300;text-transform:uppercase;letter-spacing:.5px}
  .on-water{color:#fff}
  .story-title{font-size:25px}
  .story-text{font-size:10.5px;line-height:1.5;font-style:italic;opacity:.95}
  .hours{text-align:center;color:#fff}
  .hours__label{font-size:14px;font-weight:600;text-transform:uppercase;letter-spacing:.5px;margin-top:14px}
  .hours__line{font-size:15px;font-weight:300}
  .brand{font-weight:600;font-size:30px;color:var(--ink);display:flex;align-items:center;gap:10px;justify-content:center}
  .brand__dot{width:14px;height:14px;border-radius:50%;background:var(--ocean)}
  .contact{text-align:center;font-size:15px;line-height:1.6}
  .contact__gap{margin-top:18px}
  .cover-title{font-size:33px;font-weight:300;color:#fff;letter-spacing:1px}
  .cover-tagline{font-size:13px;line-height:1.5;text-align:center}
  .cover-url{color:var(--deep);font-weight:600;letter-spacing:4px;text-align:center;font-size:14px;margin-top:14px}
  .section-title{display:flex;align-items:center;gap:8px;font-size:22px;font-weight:300;color:var(--deep);text-transform:uppercase}
  .section-title__icon{width:26px;height:26px;border-radius:50%;border:3px solid var(--deep)}
  .body-text{font-size:10px;line-height:1.5;color:var(--muted);margin-top:6px}
  .tip-box{color:#fff}
  .tip-box__title{font-size:17px;font-weight:300;text-transform:uppercase}
  .tip-box__lead{font-size:10px;margin:2px 0 10px}
  .tips{list-style:none}
  .tips li{font-size:10.5px;line-height:1.4;margin-bottom:9px;padding-left:16px;position:relative}
  .tips li::before{content:"";position:absolute;left:0;top:4px;width:8px;height:8px;border-radius:50%;background:currentColor}
  .know-title{font-size:12px;font-weight:600;color:var(--deep);text-transform:uppercase}
  .know-list{color:var(--muted);margin-top:8px}
  .know-list li::before{background:var(--ocean)}
</style>
</head>
<body>

<!-- Outside of the brochure -->
<section class="spread spread--outside">
  <svg class="artwork" viewBox="0 0 1100 850" aria-hidden="false">
    <defs>
      <linearGradient id="water" x1="0" y1="0" x2="0" y2="1">
        <stop offset="0" stop-color="#5cc3ea"/><stop offset="1" stop-color="#1f8fc5"/>
      </linearGradient>
      <linearGradient id="family" x1="0" y1="0" x2="1" y2="1">
        <stop offset="0" stop-color="#6f7b4a"/><stop offset=".5" stop-color="#a39a86"/><stop offset="1" stop-color="#5b5a4c"/>
      </linearGradient>
      <linearGradient id="swimmer" x1="0" y1="0" x2="0" y2="1">
        <stop offset="0" stop-color="#3db2e2"/><stop offset=".6" stop-color="#3aa4d4"/><stop offset="1" stop-color="#1c86bd"/>
      </linearGradient>
    </defs>
    <!-- left panel -->
    <rect role="img" aria-label="Photo of the owners with their two retrievers outdoors" x="0" y="420" width="367" height="430" fill="url(#family)"/>
    <path d="M0,0 H367 V470 C300,440 200,470 120,500 C70,518 30,520 0,505 Z" fill="url(#water)"/>
    <path d="M0,512 C30,528 70,526 120,507 C200,477 300,447 367,477" fill="none" stroke="var(--deep)" stroke-width="9"/>
    <!-- middle panel -->
    <path d="M367,0 H733 V640 C660,610 600,520 520,500 C450,482 400,480 367,480 Z" fill="url(#water)"/>
    <path d="M367,492 C400,492 450,494 520,512 C600,532 660,622 733,652" fill="none" stroke="var(--deep)" stroke-width="9"/>
    <path d="M367,510 C400,510 450,512 520,530 C600,550 660,640 733,670" fill="none" stroke="var(--ocean)" stroke-width="3"/>
    <rect role="img" aria-label="Street map showing the facility location" x="420" y="270" width="260" height="160" fill="#eef0f2"/>
    <!-- right panel / cover -->
    <rect role="img" aria-label="Photo of a yellow Labrador swimming in a blue pool" x="733" y="0" width="367" height="700" fill="url(#swimmer)"/>
    <path d="M733,850 V650 C820,640 900,600 980,560 C1030,540 1070,530 1100,530 V850 Z" fill="var(--paper)"/>
    <path d="M733,636 C820,626 900,586 980,546 C1030,526 1070,516 1100,516" fill="none" stroke="var(--ocean)" stroke-width="12"/>
    <path d="M733,616 C820,606 900,566 980,526 C1030,506 1070,496 1100,496" fill="none" stroke="var(--deep)" stroke-width="4"/>
  </svg>

  <div class="block on-water" style="left:24px;top:28px;width:320px">
    <h2 class="heading-light story-title">Our Story</h2>
    <p class="story-text">Our dream of opening a pet care business began with two dogs who loved the water. We searched for a clean, year-round place where they could swim, run and rest, and when we could not find one, we decided to build it ourselves for every family.</p>
    <h2 class="heading-light story-title" style="margin-top:26px">Our Pledge to You</h2>
    <p class="story-text">We promise a safe, spotless facility, a caring trained staff and open communication with every pet parent. Your dog will be treated like family from the moment you walk through our doors until pick-up.</p>
  </div>

  <div class="block hours" style="left:367px;top:50px;width:366px">
    <p class="hours__label">Working Hours</p>
    <p class="hours__line">7am–9pm (M–F) &amp; 9am–5pm (S–S)</p>
    <p class="hours__label">Dog Park Hours</p>
    <p class="hours__line">Tuesday – Friday: 10–1pm &amp; 4–8pm</p>
    <p class="hours__line">Saturday/Sunday: 9–5pm</p>
  </div>

  <div class="block" style="left:367px;top:560px;width:366px">
    <p class="brand"><span class="brand__dot"></span>Splash &amp; Stroll</p>
    <div class="contact contact__gap">
      <p>420 Harbor Lane</p>
      <p>Riverton IL U.S.A. 60999</p>
      <p class="contact__gap">555-014-2277</p>
      <p class="contact__gap">www.splashandstroll.com</p>
    </div>
  </div>

  <h1 class="block cover-title" style="left:733px;top:36px;width:346px;text-align:right">POOL, PARK, FUN</h1>
  <div class="block" style="left:753px;top:660px;width:327px">
    <p class="brand"><span class="brand__dot"></span>Splash &amp; Stroll</p>
    <p class="cover-tagline" style="margin-top:16px">Splash &amp; Stroll is a place for dogs and their pet parents to enjoy time together in a safe, clean, comfortable environment that encourages interactive and healthy play.</p>
    <p class="cover-url">www.splashandstroll.com</p>
  </div>
</section>

<!-- Inside of the brochure -->
<section class="spread spread--inside">
  <svg class="artwork" viewBox="0 0 1100 850">
    <defs>
      <clipPath id="below-wave"><path d="M0,250 C120,200 250,180 367,240 C450,290 560,300 733,250 C850,215 980,210 1100,200 V850 H0 Z"/></clipPath>
      <clipPath id="above-wave"><path d="M0,0 H1100 V200 C980,210 850,215 733,250 C560,300 450,290 367,240 C250,180 120,200 0,250 Z"/></clipPath>
      <linearGradient id="lawn" x1="0" y1="0" x2="0" y2="1"><stop offset="0" stop-color="#7fa35a"/><stop offset="1" stop-color="#4f7a34"/></linearGradient>
      <linearGradient id="goggles" x1="0" y1="0" x2="1" y2="1"><stop offset="0" stop-color="#f1f3f5"/><stop offset=".5" stop-color="#c9b29a"/><stop offset="1" stop-color="#e8eaec"/></linearGradient>
      <linearGradient id="grass" x1="0" y1="0" x2="0" y2="1"><stop offset="0" stop-color="#b5dc6a"/><stop offset="1" stop-color="var(--grass)"/></linearGradient>
    </defs>
    <rect role="img" aria-label="Photo of a terrier leaping across a lawn" x="0" y="120" width="367" height="310" fill="url(#lawn)" clip-path="url(#below-wave)"/>
    <rect role="img" aria-label="Photo of a terrier wearing blue swim goggles" x="367" y="0" width="366" height="320" fill="url(#goggles)" clip-path="url(#above-wave)"/>
    <rect role="img" aria-label="Photo of a beagle in a blue bandana on artificial turf" x="733" y="120" width="367" height="280" fill="url(#lawn)" clip-path="url(#below-wave)"/>
    <path d="M0,250 C120,200 250,180 367,240 C450,290 560,300 733,250 C850,215 980,210 1100,200" fill="none" stroke="var(--deep)" stroke-width="14"/>
    <path d="M0,268 C120,218 250,198 367,258 C450,308 560,318 733,268 C850,233 980,228 1100,218" fill="none" stroke="var(--ocean)" stroke-width="3"/>
    <rect role="img" aria-label="Photo of puppies playing together indoors" x="20" y="650" width="160" height="140" fill="#9fb7c4"/>
    <rect role="img" aria-label="Photo of a puppy with a colourful toy" x="188" y="650" width="160" height="140" fill="#c7a98a"/>
    <rect x="390" y="470" width="320" height="330" fill="var(--teal)"/>
    <rect role="img" aria-label="Photo of a dog swimming in the indoor pool" x="753" y="640" width="160" height="140" fill="#6fb9d6"/>
    <rect role="img" aria-label="Photo of dogs running in the outdoor yard" x="920" y="620" width="160" height="140" fill="#93b66b"/>
    <rect role="img" aria-label="Grass border" x="0" y="800" width="1100" height="50" fill="url(#grass)"/>
  </svg>

  <div class="block" style="left:22px;top:20px;width:325px">
    <h2 class="section-title"><span class="section-title__icon"></span>Dog Park</h2>
    <p class="body-text">Our indoor dog park is one of the first of its kind in the area. The climate controlled floor is soft, seamless and easy on joints, with play equipment for climbing, jumping and running. Benches and fresh water are always nearby so you can relax and watch the fun.</p>
    <p class="body-text">Now Open! A 2,500 square foot outdoor area that you and your dog can access through the indoor park.</p>
  </div>

  <div class="block" style="left:22px;top:455px;width:325px">
    <h2 class="section-title"><span class="section-title__icon"></span>Puppy Preschool</h2>
    <p class="body-text">Play is a crucial part of a dog's development. The earlier a puppy is introduced to other puppies and new play styles, the quicker they learn good manners. Preschool is open to puppies 12 to 24 weeks with current vaccinations. Small groups meet with a trained staff member who guides play and keeps every session positive.</p>
  </div>

  <div class="block" style="left:390px;top:320px;width:320px">
    <h2 class="section-title"><span class="section-title__icon"></span>Dog Pool</h2>
    <p class="body-text">Swimming is a great form of exercise that has been used for centuries. Our warm indoor pools offer low impact movement that builds strength, eases stiff joints and burns energy. Staff stay in the water with every swimmer, so dogs of all ages and skill levels can paddle safely.</p>
  </div>

  <div class="block tip-box" style="left:408px;top:488px;width:286px">
    <h3 class="tip-box__title">Make Pool Time the Best Time</h3>
    <p class="tip-box__lead">To make the most of your appointment, here are a few guidelines to follow:</p>
    <ul class="tips">
      <li>Be honest about the health of your dog.</li>
      <li>Arrive 5–10 minutes before your swim time.</li>
      <li>Lightly brush your dog before entering the pool.</li>
      <li>Do not feed your dog for at least an hour before swimming.</li>
      <li>Bring a towel; your dog may still be damp after drying.</li>
      <li>Ask us about any questions or concerns you may have.</li>
    </ul>
  </div>

  <div class="block" style="left:755px;top:20px;width:325px">
    <h2 class="section-title"><span class="section-title__icon"></span>Dog Daycare</h2>
    <p class="body-text">Welcome to Pup Academy, our full day daycare program. Dogs enjoy supervised group play in our indoor park, rest time in quiet suites and plenty of attention from our team. We guarantee your dog will come home happy, tired and ready for a cozy evening.</p>
  </div>

  <div class="block" style="left:755px;top:418px;width:325px">
    <h3 class="know-title">What You Should Know About Pup Academy</h3>
    <ul class="tips know-list">
      <li>Daycare is offered Monday through Friday.</li>
      <li>A free evaluation is required before the first day.</li>
      <li>Drop-off is between 7am and 9am.</li>
      <li>Pick-up is any time before 6pm.</li>
      <li>Bring lunch for your dog, labeled with their name.</li>
      <li>Cancel at least 24 hours ahead to avoid a fee.</li>
    </ul>
  </div>
</section>

</body>
</html>
```